Employees at R&T Gale Power Services need new modern business cards

We need new business cards that showcase our new rebranded logo. We are seeking modern, clean, fresh, attractive cards while still being professional. We want to stand out. A little bit about us: we work in Canada and the USA. We offer Technical Field Advisors to support wind turbine manufacturers through the construction phase of wind farms. I am attaching a mock inspiration picture to lead you in the direction we want to see this go. Also, FYI We have approx. 10/11 different employees that would need their own card. Let me know when you would need everyone's name. We would love to see some black and white options as well as color copies- when using colors we want green to be the dominant color with accents for blue and orange (colors should match our logo). I have also attached copies of our old business card for reference.

Contact Information for Business Card

Name, Telephone, Email, address, company name, website. EXAMPLE: Dean Whitlock, DeanWhitlock@randtgale.net, 555-384-9162, 318276 Fallow Line #7, Marrowby, ON X9Z 4Q2, www.randtgale.net

Colors
0054AA
0677BA
7BADD7
CADEEF
E8F1F8
00AB8E
00BBA5
67D7C9
C6EFE9
E9F9F6
F0912C
F2A743
F7CA91
FBE8D2
FDF5EE

Requirements
Must have
• 2 sided business card

```html
<!DOCTYPE html>
<html lang="en">
<head>
<meta charset="utf-8">
<title>R&amp;T Gale Power Services – Business Card</title>
<link rel="stylesheet" href="https://fonts.googleapis.com/css2?family=Montserrat:wght@400;500;700;800&display=swap">
<style>
  :root {
    --bg-top: #d4d4d4;
    --bg-bottom: #9e9e9e;
    --card: #262626;
    --card-edge: #1c1c1c;
    --green: #3db54a;
    --orange: #f7a21b;
    --orange-deep: #f08c2a;
    --blue: #1b87cf;
    --text: #f2f2f2;
    --emboss: #2c2c2c;
  }
  * { margin: 0; padding: 0; box-sizing: border-box; }
  html, body { width: 1200px; height: 788px; overflow: hidden; }
  body {
    background: linear-gradient(180deg, var(--bg-top), var(--bg-bottom));
    font-family: "Montserrat", sans-serif;
    color: var(--text);
    position: relative;
  }
  .card {
    position: absolute;
    left: 300px;
    width: 600px;
    height: 343px;
    background: var(--card);
    border-radius: 22px;
    overflow: hidden;
    box-shadow: 0 14px 30px rgba(0,0,0,0.35);
  }
  .card--front { top: 36px; }
  .card--back { top: 409px; }

  .edge-band {
    position: absolute;
    left: 0; bottom: 0;
    width: 600px; height: 14px;
  }

  /* front */
  .brand {
    position: absolute;
    left: 44px; top: 58px;
    display: flex; align-items: center; gap: 12px;
  }
  .brand__dot {
    width: 30px; height: 30px; border-radius: 50%;
    background: var(--green);
  }
  .brand__name {
    font-weight: 800; font-size: 17px; letter-spacing: 1.5px;
    color: var(--green); text-transform: uppercase;
  }
  .person { position: absolute; left: 44px; top: 138px; }
  .person__name {
    font-weight: 800; font-size: 27px; letter-spacing: 2px;
    color: var(--green); text-transform: uppercase;
  }
  .person__title { font-size: 15px; font-weight: 500; margin-top: 4px; letter-spacing: 0.5px; }
  .divider {
    position: absolute; left: 322px; top: 126px;
    width: 1px; height: 84px; background: var(--orange);
  }
  .contacts {
    position: absolute; left: 340px; top: 122px;
    list-style: none; font-size: 13px; font-weight: 500; letter-spacing: 0.3px;
  }
  .contacts li { display: flex; align-items: center; gap: 8px; height: 29px; }
  .contacts svg { width: 13px; height: 13px; flex: none; }
  .address {
    position: absolute; left: 44px; top: 258px;
    font-size: 14.5px; font-weight: 500; letter-spacing: 0.5px;
  }

  /* back */
  .back-disc {
    position: absolute; left: 210px; top: 36px;
    width: 180px; height: 180px; border-radius: 50%;
    background: var(--emboss);
    box-shadow: inset 3px 4px 8px rgba(0,0,0,0.55), inset -2px -2px 6px rgba(255,255,255,0.05);
  }
  .back-name {
    position: absolute; right: 40px; top: 262px;
    font-weight: 800; font-size: 26px; letter-spacing: 2px;
    color: var(--green); text-transform: uppercase;
  }
</style>
</head>
<body>

<section class="card card--front" aria-label="Business card front">
  <div class="brand">
    <span class="brand__dot"></span>
    <span class="brand__name">R&amp;T Gale Power Services</span>
  </div>

  <div class="person">
    <p class="person__name">Dean Whitlock</p>
    <p class="person__title">CEO/Founder</p>
  </div>

  <span class="divider"></span>

  <ul class="contacts">
    <li>
      <svg viewBox="0 0 24 24" aria-hidden="true"><path fill="#f7a21b" d="M6.6 10.8a15 15 0 0 0 6.6 6.6l2.2-2.2c.3-.3.7-.4 1-.2 1.1.4 2.3.6 3.6.6.6 0 1 .4 1 1V20c0 .6-.4 1-1 1A17 17 0 0 1 3 4c0-.6.4-1 1-1h3.5c.6 0 1 .4 1 1 0 1.3.2 2.5.6 3.6.1.3 0 .7-.2 1z"/></svg>
      555-384-9162
    </li>
    <li>
      <svg viewBox="0 0 24 24" aria-hidden="true"><path fill="#f7a21b" d="M2 5h20v14H2z"/><path fill="none" stroke="#262626" stroke-width="2" d="M2 5l10 8 10-8"/></svg>
      DeanWhitlock@randtgale.net
    </li>
    <li>
      <svg viewBox="0 0 24 24" aria-hidden="true"><circle cx="12" cy="12" r="10" fill="#f7a21b"/><path fill="none" stroke="#262626" stroke-width="1.5" d="M2 12h20M12 2c3 3 3 17 0 20M12 2c-3 3-3 17 0 20"/></svg>
      www.randtgale.net
    </li>
  </ul>

  <p class="address">318276 Fallow Line #7, Marrowby, ON X9Z 4Q2</p>

  <svg class="edge-band" viewBox="0 0 600 14" preserveAspectRatio="none" aria-hidden="true">
    <defs>
      <linearGradient id="orangeFront" x1="0" x2="1">
        <stop offset="0" stop-color="#f08c2a"/><stop offset="0.5" stop-color="#fcc419"/><stop offset="1" stop-color="#f08c2a"/>
      </linearGradient>
    </defs>
    <polygon points="0,0 252,0 240,14 0,14" fill="#3db54a"/>
    <polygon points="256,0 478,0 466,14 244,14" fill="url(#orangeFront)"/>
    <polygon points="482,0 600,0 600,14 470,14" fill="#1b87cf"/>
  </svg>
</section>

<section class="card card--back" aria-label="Business card back">
  <span class="back-disc"></span>
  <p class="back-name">R&amp;T Gale Power Services</p>

  <svg class="edge-band" viewBox="0 0 600 14" preserveAspectRatio="none" aria-hidden="true">
    <defs>
      <linearGradient id="orangeBack" x1="0" x2="1">
        <stop offset="0" stop-color="#f08c2a"/><stop offset="0.5" stop-color="#fcc419"/><stop offset="1" stop-color="#f08c2a"/>
      </linearGradient>
    </defs>
    <polygon points="0,0 206,0 194,14 0,14" fill="#3db54a"/>
    <polygon points="210,0 448,0 436,14 198,14" fill="url(#orangeBack)"/>
    <polygon points="452,0 600,0 600,14 440,14" fill="#1b87cf"/>
  </svg>
</section>

</body>
</html>
```